New Zealand Luggage Importer Needs Business Cards

We need professional, creative and fashionable business cards created.
We are based in New Zealand and import and distribute high-end, quality, fashionable and durable luggage.
We pride ourselves on selling the very best quality luggage, second only to 1 brand (which we won't mention here)...we use the same manufacturer. However, our prices are much more reasonable.
Industry/Entity Type
Business
Contact Information for Business Card
Mark Dunsley
027 512 4068
3/17 Harlow Street, Pinecrest Flats, Auckland, 0614
PO Box 204377, Fernside, Auckland 0731
09-528-3916
sales@brivancases.co.nz / www.brivancases.co.nz

```html
<!DOCTYPE html>
<html lang="en">
<head>
<meta charset="utf-8">
<title>Brivan Cases – Business Card</title>
<link rel="stylesheet" href="https://fonts.googleapis.com/css2?family=Bebas+Neue&family=Oswald:wght@300;400&display=swap">
<style>
  :root {
    --backdrop: #9a9a9a;
    --navy-deep: #04123a;
    --navy: #0a2a63;
    --sky: #5ab4e6;
    --sky-pale: #d6ecfa;
    --band-blue: #1f9bd9;
    --name-blue: #4fb9d9;
    --gold: #c9a86a;
    --ink: #111111;
    --grey-text: #6a6a6a;
    --white: #ffffff;
  }
  * { margin: 0; padding: 0; box-sizing: border-box; }
  html, body { width: 1200px; height: 1200px; overflow: hidden; }
  body {
    background: var(--backdrop);
    position: relative;
    font-family: "Oswald", sans-serif;
  }
  .card {
    position: absolute;
    left: 236px;
    width: 728px;
    height: 416px;
    overflow: hidden;
  }
  .card--front { top: 144px; background: var(--navy-deep); }
  .card--back { top: 630px; background: var(--white); }

  .tile-field {
    position: absolute;
    inset: 0;
  }
  .card--front .tile-field {
    background:
      radial-gradient(ellipse 70% 75% at 0% 0%, rgba(90,180,230,0.75), rgba(20,70,140,0.45) 45%, rgba(4,18,58,0) 80%),
      linear-gradient(160deg, var(--navy) 0%, var(--navy-deep) 70%);
  }
  .card--back .tile-field {
    background:
      radial-gradient(ellipse 75% 90% at 100% 45%, rgba(150,205,240,0.7), rgba(214,236,250,0.5) 45%, rgba(255,255,255,0) 80%);
  }

  .web-band {
    position: absolute;
    left: 0;
    top: 276px;
    width: 728px;
    height: 48px;
  }
  .card--back .web-band { top: 204px; }
  .web-band svg { display: block; }
  .web-address {
    position: absolute;
    right: 38px;
    top: 0;
    line-height: 48px;
    font-family: "Bebas Neue", sans-serif;
    font-size: 34px;
    color: var(--white);
    letter-spacing: 0.2px;
  }

  .brand-name {
    position: absolute;
    right: 44px;
    top: 212px;
    font-family: "Bebas Neue", sans-serif;
    font-size: 42px;
    letter-spacing: 3px;
    color: var(--gold);
  }

  .holder-name {
    position: absolute;
    left: 58px;
    top: 80px;
    font-family: "Bebas Neue", sans-serif;
    font-size: 58px;
    line-height: 1;
    color: var(--name-blue);
  }
  .holder-mobile {
    position: absolute;
    left: 61px;
    top: 136px;
    font-family: "Oswald", sans-serif;
    font-size: 14px;
    color: var(--ink);
  }
  .company-address {
    position: absolute;
    left: 246px;
    top: 266px;
    font-family: "Oswald", sans-serif;
    font-weight: 300;
    font-size: 16px;
    line-height: 24px;
    color: var(--grey-text);
    text-transform: uppercase;
    white-space: nowrap;
  }
  .company-address .indent { padding-left: 4px; }
</style>
</head>
<body>

  <section class="card card--front">
    <div class="tile-field" role="img" aria-label="Perspective tiled floor pattern fading from light blue into navy"></div>
    <div class="brand-name">Brivan Cases</div>
    <div class="web-band">
      <svg width="728" height="48" viewBox="0 0 728 48">
        <defs>
          <linearGradient id="frontBand" x1="0" x2="1">
            <stop offset="0" stop-color="#1d4f8c" stop-opacity="0"/>
            <stop offset="0.3" stop-color="#1d4f8c"/>
            <stop offset="1" stop-color="#5ab4e6"/>
          </linearGradient>
        </defs>
        <rect x="150" y="34" width="240" height="10" fill="#1d4f8c" opacity="0.35"/>
        <polygon points="352,0 728,0 728,48 330,48 340,40" fill="url(#frontBand)"/>
      </svg>
      <span class="web-address">www.brivancases.co.nz</span>
    </div>
  </section>

  <section class="card card--back">
    <div class="tile-field" role="img" aria-label="Pale blue perspective tiled floor pattern on the right side"></div>
    <h1 class="holder-name">MARK DUNSLEY</h1>
    <p class="holder-mobile">MOBILE :- 027 512 4068</p>
    <div class="web-band">
      <svg width="728" height="48" viewBox="0 0 728 48">
        <defs>
          <linearGradient id="backBand" x1="0" x2="1">
            <stop offset="0" stop-color="#bfe3f6"/>
            <stop offset="1" stop-color="#1f9bd9"/>
          </linearGradient>
          <linearGradient id="backStreak" x1="0" x2="1">
            <stop offset="0" stop-color="#bfe3f6" stop-opacity="0"/>
            <stop offset="1" stop-color="#bfe3f6"/>
          </linearGradient>
        </defs>
        <rect x="110" y="0" width="222" height="8" fill="url(#backStreak)"/>
        <polygon points="332,0 728,0 728,48 372,48" fill="url(#backBand)"/>
      </svg>
      <span class="web-address">www.brivancases.co.nz</span>
    </div>
    <address class="company-address">
      Your address,3/17 Harlow Street, Pinecrest Flats, Auckland, 0614<br>
      PO Box 204377, Fernside,<br>
      <span class="indent">Auckland 0731</span><br>
      Tel: 09-528-3916
    </address>
  </section>

</body>
</html>
```